PowerPoint template design needed for sales and presales presentations

We would like to have a bright and light, contemporary PowerPoint design based on our existing style assets (see attached files).
We are based in Latvia. Our business is ERP systems implementation, IT infrastructure building and supporting our customers. We are moving from traditional Add-hoc projects model to standardized flat-rate offerings. Our technology platform is Dravomell.
The value proposition of our offerings is based around simplicity, transparency, quality, peace of mind, trust, easy of doing business.
I have to add that if any special are being used, they must be unicode to ensure proper Latvian language characters display.
Updates
Hi! The reason is an error at your side. Today it's 24/08/2020 when I started the project and made a payment. Still for some funny reason in the BRIEF I see that the project deadline is set to 20/08/2020. No wonder no designers are applying...
Target Market(s)
Small and medium enterprise
Look and feel
Each slider illustrates characteristics of the customer's brand and the style your logo design should communicate.

```html
<!DOCTYPE html>
<html lang="en">
<head>
<meta charset="utf-8">
<title>Kalnova Digital – Presentation Template</title>
<link href="https://fonts.googleapis.com/css2?family=Barlow:wght@400;500;600&display=swap" rel="stylesheet">
<style>
  :root {
    --board: #c8c8c8;
    --ink: #07080b;
    --ink-soft: #1b1d23;
    --teal: #00b8b5;
    --green: #8bc43f;
    --yellow: #fdc80a;
    --white: #ffffff;
    --lavender: #e9e9f9;
    --mist: #d9dae2;
    --line-grey: #6d6f76;
    --frame-grey: #8a8a8a;
  }
  * { margin: 0; padding: 0; box-sizing: border-box; }
  html, body {
    width: 1200px;
    height: 1200px;
    overflow: hidden;
    background: var(--board);
    font-family: "Barlow", "Helvetica Neue", Arial, sans-serif;
    color: var(--ink);
  }
  .board { position: relative; width: 1200px; height: 1200px; }
  .slide-label {
    position: absolute;
    font-size: 10.5px;
    font-weight: 400;
    letter-spacing: 0.1px;
  }
  .slide-label--front { left: 370px; top: 168px; }
  .slide-label--topics { left: 377px; top: 599px; }
  .ratio-note { position: absolute; left: 823px; top: 912px; font-size: 10.5px; font-weight: 400; }
  .slide { position: absolute; display: block; }
  .slide--front { left: 365px; top: 196px; width: 461px; height: 259px; }
  .slide--topics { left: 374px; top: 630px; width: 461px; height: 260px; }
  .t-title { font-weight: 500; fill: var(--ink); }
  .t-sub { font-weight: 500; fill: var(--teal); }
  .t-brand { font-weight: 600; fill: var(--white); letter-spacing: 1px; }
  .t-bar-title { font-weight: 500; fill: var(--white); }
  .t-bar-sub { font-weight: 600; fill: var(--ink); }
  .t-body { font-weight: 400; fill: var(--ink); }
</style>
</head>
<body>
<main class="board">

  <p class="slide-label slide-label--front">Front Presentation</p>

  <svg class="slide slide--front" viewBox="0 0 742 417" preserveAspectRatio="none" aria-label="Title slide">
    <defs>
      <radialGradient id="front-glow" cx="0.5" cy="0.55" r="0.75">
        <stop offset="0.55" stop-color="#ffffff"/>
        <stop offset="1" stop-color="#e6e6f8"/>
      </radialGradient>
    </defs>
    <rect class="front-bg" width="742" height="417" fill="url(#front-glow)"/>

    <polygon points="18,0 170,10 88,105 0,22" fill="var(--lavender)"/>
    <polyline points="18,0 0,20 88,106 175,18" fill="none" stroke="var(--teal)" stroke-width="2"/>

    <polygon class="texture-left" role="img" aria-label="Striped texture area" points="0,40 110,150 74,198 0,124" fill="var(--mist)"/>

    <polygon class="stripe-teal" points="213,0 250,0 113,134 96,120" fill="var(--teal)"/>
    <polygon class="band-black" points="250,0 618,0 235,383 53,203" fill="var(--ink)"/>
    <polygon class="stripe-green" points="618,0 638,0 388,252 374,254" fill="var(--green)"/>

    <polygon class="texture-band" role="img" aria-label="Fine line texture area" points="380,0 485,0 360,125 290,90" fill="var(--ink-soft)"/>

    <polygon points="235,36 397,200 235,381 53,204" fill="var(--ink)"/>
    <polygon points="235,36 397,200 235,381 53,204" fill="none" stroke="var(--line-grey)" stroke-width="1"/>

    <polygon points="0,162 33,199 0,233" fill="var(--green)"/>
    <polygon points="0,300 36,264 188,417 0,417" fill="var(--yellow)"/>
    <polyline points="0,249 36,214 218,396 198,417" fill="none" stroke="var(--yellow)" stroke-width="3"/>
    <polygon points="333,307 443,417 223,417" fill="var(--teal)"/>

    <polygon points="600,74 742,214 590,400 420,256" fill="none" stroke="#f3f0dc" stroke-width="2"/>

    <text class="t-brand" x="232" y="207" font-size="19" text-anchor="middle">KALNOVA DIGITAL</text>

    <text class="t-title" x="722" y="298" font-size="28.5" text-anchor="end">TITLE PRESENTATION HERE</text>
    <text class="t-sub" x="717" y="332" font-size="18.5" text-anchor="end">Subtitle Here</text>

    <g class="tabs">
      <rect x="733" y="4" width="9" height="23" fill="var(--ink)"/>
      <rect x="733" y="42" width="9" height="23" fill="var(--teal)"/>
      <rect x="733" y="81" width="9" height="23" fill="var(--green)"/>
      <rect x="733" y="119" width="9" height="23" fill="var(--yellow)"/>
      <rect x="733" y="277" width="9" height="23" fill="var(--ink)"/>
      <rect x="733" y="315" width="9" height="23" fill="var(--teal)"/>
      <rect x="733" y="354" width="9" height="23" fill="var(--green)"/>
      <rect x="733" y="392" width="9" height="23" fill="var(--yellow)"/>
    </g>
  </svg>

  <p class="slide-label slide-label--topics">Topics Presentation</p>

  <svg class="slide slide--topics" viewBox="0 0 743 418" preserveAspectRatio="none" aria-label="Topics slide">
    <rect width="743" height="418" fill="var(--white)" stroke="var(--frame-grey)" stroke-width="1.5"/>

    <rect x="0" y="31" width="299" height="30" fill="var(--ink)"/>
    <line x1="8" y1="56" x2="24" y2="56" stroke="var(--white)" stroke-width="1.5"/>
    <text class="t-bar-title" x="43" y="52" font-size="20">TITLE PRESENTATION HERE</text>
    <rect x="0" y="66" width="186" height="19" fill="var(--teal)"/>
    <text class="t-bar-sub" x="43" y="79" font-size="13">Subtitle Here</text>

    <rect x="0" y="98" width="16" height="19" fill="var(--green)"/>
    <rect x="0" y="130" width="16" height="19" fill="var(--yellow)"/>
    <rect x="0" y="162" width="16" height="19" fill="var(--ink)"/>
    <rect x="0" y="195" width="16" height="19" fill="var(--teal)"/>
    <rect x="0" y="227" width="16" height="19" fill="var(--green)"/>
    <rect x="0" y="260" width="16" height="19" fill="var(--yellow)"/>

    <text class="t-body" x="61" y="117" font-size="16.5">Topic 1</text>
    <g class="t-body" font-size="16.8">
      <circle cx="78" cy="142" r="3" fill="var(--ink)"/><text x="89" y="148">Lorem ipsum dolor sit amet, consectetur adipiscing elit.</text>
      <circle cx="78" cy="169" r="3" fill="var(--ink)"/><text x="89" y="175">Maecenas tempus ligula in magna semper, eu lobortis nibh vulputate.</text>
      <circle cx="78" cy="195" r="3" fill="var(--ink)"/><text x="89" y="201">Donec at ligula suscipit, pharetra nisi vel, molestie lorem.</text>
      <circle cx="78" cy="222" r="3" fill="var(--ink)"/><text x="89" y="228">Duis a ipsum sollicitudin, rutrum justo vehicula, dictum enim.</text>
      <circle cx="78" cy="249" r="3" fill="var(--ink)"/><text x="89" y="255">Nunc vel massa imperdiet urna porta ultricies et id urna.</text>
      <circle cx="78" cy="275" r="3" fill="var(--ink)"/><text x="89" y="281">Donec vitae nisl iaculis, elementum eros ut, dignissim velit.</text>
    </g>

    <polygon points="0,283 58,343 0,396" fill="var(--teal)"/>
    <polygon class="texture-corner" role="img" aria-label="Striped texture area" points="52,348 122,418 14,418 20,380" fill="var(--mist)"/>
    <polygon points="12,418 28,402 44,418" fill="var(--green)"/>

    <polygon points="381,376 424,418 338,418" fill="var(--ink)"/>
    <polyline points="488,418 523,384 558,418" fill="none" stroke="var(--yellow)" stroke-width="3"/>

    <polygon points="743,138 743,163 573,331 561,319" fill="var(--yellow)"/>
    <polygon points="531,376 743,166 743,418 573,418" fill="var(--ink)"/>
    <polygon points="660,262 743,345 743,418 580,418 547,385" fill="none" stroke="var(--line-grey)" stroke-width="1"/>
    <polygon class="texture-band" role="img" aria-label="Fine line texture area" points="743,220 743,260 720,283 700,263" fill="var(--ink-soft)"/>

    <text class="t-brand" x="652" y="381" font-size="13" text-anchor="middle">KALNOVA DIGITAL</text>
  </svg>

  <p class="ratio-note">16:9</p>

</main>
</body>
</html>
```